Cloud Hosted Phone System for small and medium sized businesses

I want to design a one A4 page size single or double sided brochure to offer cloud hosted VoIP Phone system and a complete collaboration system. We have partnered with a VoIP Phone system company and want to sell their services but we don't want their name to be shown on the brochure because customers might call them directly. The company name is Corvane (www.corvane-example.com) and our company name is KESTRAL Tech Solutions. I have also uploaded my compnay's logo that you should show on the brochure. For more details about the product, you can visit their website as mentioned above.

Reason: Not getting a design to my liking.

Target Market(s)

Small and medium sized business including law firms, marketing and advertising agencies, real-estate firms and others.

Industry/Entity Type

Voip

Colors

Designer to choose colors to be used in the design.

Requirements
Must have
• My company's Logo (KESTRAL Tech Solutions). Price list, services and some images to show the benefits and services of the cloud based and advanced VoIP phone system. I want the brochure to look very professional and attractive.
• Contact US: Our company's name, Logo, web address, phone (555-371-9046) and email (info@kestraltechsolutions-example.com)
Nice to have
• It is a Canadian based company and all of our servers and customers’ data reside in Canada.

```html
<!DOCTYPE html>
<html lang="en">
<head>
<meta charset="utf-8">
<title>KESTRAL Tech Solutions – Cloud-Based Phone System</title>
<link rel="stylesheet" href="https://fonts.googleapis.com/css2?family=Source+Sans+3:wght@400;600;700;800;900&display=swap">
<style>
  :root{
    --navy:#1c2d47;
    --blue:#1f4f88;
    --sky:#cfe6f6;
    --ink:#1e1e1e;
    --grey-panel:rgba(72,80,92,.9);
    --white:#ffffff;
    --footer-soft:#d9e6f3;
  }
  *{box-sizing:border-box;margin:0;padding:0}
  html,body{width:1200px;height:3390px;overflow:hidden;background:var(--white)}
  body{position:relative;font-family:"Source Sans 3",Arial,sans-serif;color:var(--ink)}
  .abs{position:absolute}

  /* brand */
  .brand{display:flex;align-items:center;gap:18px}
  .brand-dot{width:128px;height:128px;border-radius:50%;background:var(--blue)}
  .brand-name{color:var(--navy);font-weight:600;line-height:.95}
  .brand-name .big{display:block;font-size:82px;letter-spacing:1px}
  .brand-name .small{display:block;font-size:42px;margin-top:4px}

  /* page one */
  .hero-title{left:36px;top:318px;color:var(--white);font-weight:800;font-size:58px;line-height:54px;letter-spacing:1px;white-space:nowrap}
  .hero-copy{left:36px;top:432px;color:var(--white);font-size:20.5px;line-height:24px;white-space:nowrap}
  .benefits-title{left:36px;top:648px;color:var(--navy);font-weight:800;font-size:37px;line-height:1;white-space:nowrap}
  .benefits-rule{left:36px;top:688px;width:780px;height:2px;background:var(--navy)}
  .benefit h3{color:var(--navy);font-weight:800;font-size:26px;line-height:26px;text-decoration:underline;text-underline-offset:3px;white-space:nowrap}
  .benefit p{font-size:19px;line-height:21px;margin-top:2px;white-space:nowrap}
  .canada-note{left:65px;top:1392px;width:300px;text-align:center;color:var(--white);font-size:29px;line-height:32px}
  .canada-rule{left:90px;top:1644px;width:250px;height:2px;background:var(--white)}
  .canada-diamond{left:206px;top:1636px;width:17px;height:17px;background:var(--white);transform:rotate(45deg)}
  .offer-title{left:690px;top:1082px;width:500px;text-align:center;color:var(--navy);font-weight:800;font-size:37px;line-height:45px}
  .offer-rule{left:655px;top:1178px;width:545px;height:3px;background:var(--navy)}
  .service{right:142px;width:620px;text-align:right;white-space:nowrap}
  .service h4{font-weight:700;font-size:28px;line-height:32px;color:var(--ink)}
  .service p{font-size:22px;line-height:26px}
  .service-icon{left:1088px;width:72px;height:72px}

  /* page two */
  .features-title{left:36px;top:2004px;color:var(--white);font-weight:800;font-size:62px;line-height:1;letter-spacing:1px;text-decoration:underline;text-decoration-thickness:3px;text-underline-offset:6px;white-space:nowrap}
  .features-list{left:44px;top:2082px;list-style:none;color:var(--white);font-weight:800;font-size:26px;line-height:34.2px;letter-spacing:1.5px;white-space:nowrap}
  .features-list li::before{content:"•";margin-right:14px}
  .features-list li.more::before{content:"";margin-right:40px}
  .plans-banner{left:690px;top:2565px;width:510px;height:92px;background:var(--navy);color:var(--white);font-weight:800;font-size:58px;display:flex;align-items:center;justify-content:center;letter-spacing:1px}
  .plan-tab{top:2723px;height:91px;border:2px solid var(--navy);border-bottom:none;border-radius:44px 44px 0 0;background:var(--white);color:var(--navy);font-weight:800;font-size:40px;display:flex;align-items:flex-end;justify-content:center;padding-bottom:10px;letter-spacing:1px}
  .plan-tab.featured{top:2662px;height:152px;background:var(--navy);color:var(--white);border-radius:110px 110px 0 0;flex-direction:column;align-items:center;justify-content:flex-end}
  .plan-tab .badge{font-size:18px;font-weight:600;letter-spacing:1px;margin-bottom:4px}
  .plans-table{left:38px;top:2814px;width:1126px;border-collapse:collapse;font-size:22px}
  .plans-table td{height:57px;border:2px solid var(--navy);padding:0 12px;text-align:center}
  .plans-table td.label{text-align:left;width:407px}
  .plans-table tr.tint td{background:var(--sky)}
  .plans-table tr.sub td{border-left:none;border-right:none}
  .plans-table tr.sub td.label{border-left:2px solid var(--navy)}
  .plans-table tr.sub td:last-child{border-right:2px solid var(--navy)}
  .footer{left:0;top:3232px;width:1200px;height:158px;background:var(--navy);text-align:center;color:var(--white)}
  .footer .contact{font-size:36px;letter-spacing:1.5px;line-height:40px;margin-top:32px;color:var(--footer-soft)}
  .footer .web{font-size:46px;font-weight:800;letter-spacing:2px;line-height:56px}
</style>
</head>
<body>

<!-- ===== Page one ===== -->
<section class="page page-one">
  <div class="abs" style="left:600px;top:0;width:600px;height:680px;background:linear-gradient(200deg,#cfd4d9 0%,#e9ecef 55%,#ffffff 100%)" role="img" aria-label="Desk IP phone close-up photograph"></div>

  <svg class="abs" style="left:0;top:0" width="1200" height="1668" viewBox="0 0 1200 1668" aria-hidden="true">
    <polygon points="0,267 813,267 800,290 0,290" fill="#1c2d47"/>
    <polygon points="0,290 800,290 700,633 0,633" fill="#1f4f88" fill-opacity=".92"/>
    <polygon points="0,1420 690,1040 1200,1040 1200,1668 0,1668" fill="#1c2d47"/>
    <polygon points="650,1064 1200,1064 1200,1652 390,1652" fill="#ffffff"/>
  </svg>

  <div class="abs brand" style="left:34px;top:66px">
    <div class="brand-dot"></div>
    <div class="brand-name"><span class="big">KESTRAL</span><span class="small">Tech Solutions</span></div>
  </div>

  <h1 class="abs hero-title">A CLOUD-BASED PHONE<br>SYSTEM FOR BUSINESSES</h1>
  <p class="abs hero-copy">We can help you grow your business by modernizing your company’s phone<br>system and making it easy to use, manage, and track directly from the cloud<br>Our cloud business phone system adapts to your economic challenges<br>and brings flexibility and adaptability to your business communications<br>whilst considerably reducing costs compared to traditional phone<br>systems. We take great pride in continually improving our platform as<br>well as developing new features and services that in turn increase our<br>customers’ productivity.</p>

  <h2 class="abs benefits-title">BENEFITS OF CLOUD-BASED PHONE SYSTEM</h2>
  <div class="abs benefits-rule"></div>

  <div class="abs" style="left:955px;top:746px;width:200px;height:290px;background:linear-gradient(160deg,#e4e8ec,#b5bdc6)" role="img" aria-label="Hand holding a smartphone showing a dial pad"></div>

  <div class="abs benefit" style="left:36px;top:696px">
    <h3>BECOME MOBILE</h3>
    <p>From our cloud-based telephony and its unified communications system emerges the concept of mobility.<br>Make calls using your office phone, computer, or mobile phone, and chat with your colleagues and<br>customers from numerous locations. Enjoy centralized communications and simplified management.</p>
  </div>
  <div class="abs benefit" style="left:36px;top:795px">
    <h3>SAVE COSTS</h3>
    <p>The fixed and operating costs of your business communications are substantially reduced,<br>and we take care of installing, configuring, and managing your phone system.<br>Call us today for free consultation</p>
  </div>
  <div class="abs benefit" style="left:36px;top:897px">
    <h3>STAY ABREAST</h3>
    <p>Enjoy leading-edge telecommunications technology and its host of features that<br>adapt to your needs, whatever the size of your business. These features are<br>constantly upscaled and automatically updated. You will thus never have to<br>operate an obsolete system.</p>
  </div>
  <div class="abs benefit" style="left:36px;top:1019px">
    <h3>AVOID INCONVENIENCES</h3>
    <p>We take charge of the structure of your business phone system<br>and remove the PBX (Private Branch Exchange) system<br>to host it in its cloud database, thus saving you space,<br>time, and costs. You are cleared of wire clutter and<br>your business communications are streamlined,<br>allowing you to work freely and efficiently.<br>Also, this service includes an excellent<br>recovery and business continuity plan<br>that prevents unforeseen events,<br>such as claims or system<br>failures, from leading to<br>data loss or suspension<br>of business<br>activities.</p>
  </div>

  <p class="abs canada-note">It is a<br>Canadian<br>based company<br>and all of our<br>servers and<br>customers’ data<br>reside in Canada.</p>
  <div class="abs canada-rule"></div>
  <div class="abs canada-diamond"></div>

  <h2 class="abs offer-title">A CLOUD-BASED PHONE<br>SYSTEM FOR BUSINESSES</h2>
  <div class="abs offer-rule"></div>

  <div class="abs service" style="top:1203px"><h4>Cloud Phone System</h4><p>Your business phone system, now in the cloud.<br>Access every feature from anywhere.</p></div>
  <svg class="abs service-icon" style="top:1212px" viewBox="0 0 72 72" aria-hidden="true">
    <path d="M14 30a12 12 0 0 1 14-14a16 16 0 0 1 30 6a10 10 0 0 1-2 20H16a8 8 0 0 1-2-12z" fill="none" stroke="#1f4f88" stroke-width="3"/>
    <rect x="22" y="38" width="30" height="24" rx="3" fill="#1f4f88"/>
    <rect x="26" y="42" width="22" height="5" fill="#fff"/>
    <g fill="#fff"><circle cx="29" cy="52" r="2"/><circle cx="37" cy="52" r="2"/><circle cx="45" cy="52" r="2"/><circle cx="29" cy="58" r="2"/><circle cx="37" cy="58" r="2"/><circle cx="45" cy="58" r="2"/></g>
  </svg>

  <div class="abs service" style="top:1316px"><h4>Unified Communications</h4><p>A powerful suite of communications and<br>collaboration tools grouped under one platform.</p></div>
  <svg class="abs service-icon" style="top:1325px" viewBox="0 0 72 72" aria-hidden="true">
    <g fill="none" stroke="#1f4f88" stroke-width="2.5">
      <circle cx="36" cy="36" r="10"/><circle cx="36" cy="10" r="6"/><circle cx="60" cy="30" r="6"/><circle cx="52" cy="60" r="6"/><circle cx="20" cy="60" r="6"/><circle cx="12" cy="30" r="6"/>
      <path d="M36 16v10M54 32l-9 2M48 55l-6-10M24 55l6-10M18 32l9 2"/>
    </g>
  </svg>

  <div class="abs service" style="top:1429px"><h4>Contact Center</h4><p>Manage your different customer contact points<br>from a unified, user-friendly web interface.</p></div>
  <svg class="abs service-icon" style="top:1438px" viewBox="0 0 72 72" aria-hidden="true">
    <g fill="none" stroke="#1f4f88" stroke-width="2.5">
      <path d="M16 36a20 20 0 0 1 40 0"/>
      <rect x="10" y="34" width="10" height="16" rx="4"/><rect x="52" y="34" width="10" height="16" rx="4"/>
      <path d="M57 50c0 8-8 12-16 12"/><circle cx="38" cy="62" r="3"/>
      <path d="M22 66c4-6 24-6 28 0"/>
    </g>
  </svg>

  <div class="abs service" style="top:1542px"><h4>Relay Studio©</h4><p>A flexible yet easy-to-use online administration<br>portal to manage your business phone system.</p></div>
  <svg class="abs service-icon" style="top:1550px" viewBox="0 0 72 72" aria-hidden="true">
    <g fill="none" stroke="#1f4f88" stroke-width="2.5">
      <rect x="6" y="8" width="58" height="44" rx="3"/><path d="M6 18h58"/>
    </g>
    <g fill="#1f4f88"><circle cx="12" cy="13" r="2"/><circle cx="18" cy="13" r="2"/><circle cx="24" cy="13" r="2"/></g>
    <path d="M34 30l0 30l8-8l6 12l5-3l-6-11l11-1z" fill="#1f4f88"/>
  </svg>
</section>

<div class="abs" style="left:0;top:1668px;width:1200px;height:24px;background:var(--navy)"></div>

<!-- ===== Page two ===== -->
<section class="page page-two">
  <div class="abs" style="left:678px;top:1700px;width:522px;height:865px;background:linear-gradient(170deg,#e9ecef 0%,#c9d0d7 60%,#aab3bd 100%)" role="img" aria-label="Hand holding a smartphone with a desk phone in the background"></div>

  <div class="abs brand" style="left:34px;top:1782px">
    <div class="brand-dot"></div>
    <div class="brand-name"><span class="big">KESTRAL</span><span class="small">Tech Solutions</span></div>
  </div>

  <svg class="abs" style="left:0;top:1960px" width="760" height="790" viewBox="0 0 760 790" aria-hidden="true">
    <polygon points="0,2 746,2 730,25 0,25" fill="#1c2d47"/>
    <rect x="0" y="25" width="690" height="755" fill="rgba(72,80,92,.9)"/>
  </svg>

  <h2 class="abs features-title">INCLUDED FEATURES</h2>
  <ul class="abs features-list">
    <li>Access to our online portal</li>
    <li>Company greeting message (24h/7)</li>
    <li>Company’s directory</li>
    <li>Company and user voicemail</li>
    <li>Outbound Caller ID</li>
    <li>Voicemail to email</li>
    <li>Call forwarding</li>
    <li>Find-me/Follow-me</li>
    <li>Call waiting</li>
    <li>Automatic phone relocation</li>
    <li>Remote office calling &amp; transfering</li>
    <li>Phone queueing service</li>
    <li>Fraud Monitoring</li>
    <li>Custom Music on Hold</li>
    <li>Optional Hidden Caller ID</li>
    <li>Authorization code before dialing</li>
    <li>Remote Answer</li>
    <li>Call recording</li>
    <li class="more">...and more!</li>
  </ul>

  <div class="abs plans-banner">SERVICE PLANS</div>

  <div class="abs plan-tab" style="left:445px;width:224px">BASIC</div>
  <div class="abs plan-tab featured" style="left:673px;width:262px"><span class="badge">★ BEST SELLER ★</span>ENHANCED</div>
  <div class="abs plan-tab" style="left:939px;width:225px">PREMIUM</div>

  <table class="abs plans-table">
    <tr><td class="label">MONTHLY ACCOUNT FEE¹(per site)</td><td>$45,00</td><td>$45,00</td><td>$45,00</td></tr>
    <tr class="sub"><td class="label">MONTHLY USER FEE starting at:</td><td></td><td></td><td></td></tr>
    <tr class="tint"><td class="label">0 t0 19 users</td><td>$18,00</td><td>$20,00</td><td>$22,00</td></tr>
    <tr><td class="label">20 to 49 users</td><td>$15,00</td><td>$17,00</td><td>$19,00</td></tr>
    <tr class="tint"><td class="label">50 to 99 users</td><td>$12,00</td><td>$14,00</td><td>$16,00</td></tr>
    <tr><td class="label">100 to l99 users</td><td>$10,00</td><td>$12,00</td><td>$14,00</td></tr>
    <tr class="tint"><td class="label">200+ users</td><td>$8,00</td><td>$10,00</td><td>$12,00</td></tr>
  </table>

  <footer class="abs footer">
    <p class="contact">555-371-9046 | info@kestraltechsolutions-example.com</p>
    <p class="web">www.kestraltechsolutions-example.com</p>
  </footer>
</section>

</body>
</html>
```